Startup Consultancy - Brochure Design

This needs to be a digital and potential hardcopy of a glossy brochure, designed to really catch the eye of prospective clients and draw them in. I am looking for something alternative from the "usual", but equally in keeping with the IT industry that the business operate in. The business specifically focuses on Print & Document Software and Technology solutions, and this should be considered in the design.

Target Market(s)

SMB and Corporate End Users, + Technology Resellers

Industry/Entity Type

Information Technology

Other font styles liked:
• Avenir

Colors
9d9d9d
848484
c3c3c3
e8e8e8
ffffff
eaeaea
0255a3
3176b5
85acd3

Requirements
Must have
• Company logo displayed on the front, plus any other relevant placements in pages
• Must follow the colour/style in some way of the website (www.brantwellconsultancy.co.uk)
Nice to have
• Some kind of infographical style in the brochure would be good, perhaps around the service listings

```html
<!DOCTYPE html>
<html lang="en">
<head>
<meta charset="utf-8">
<title>Strategy Design Services – Brochure Spread</title>
<link rel="stylesheet" href="https://fonts.googleapis.com/css2?family=Roboto:ital,wght@0,300;0,400;0,500;0,700;1,400;1,700&display=swap">
<style>
  :root {
    --canvas: #d6d6d6;
    --slate-dark: #2b3040;
    --slate: #4a5066;
    --slate-light: #5d6479;
    --card: rgba(160,164,176,0.55);
    --card-line: rgba(255,255,255,0.85);
    --icon-blue: #3b4fa3;
    --white: #ffffff;
    --ink: #3d4250;
    --ink-soft: #4a4f5c;
    --rule-grey: #e8e8e8;
    --band: #3a3d46;
  }
  * { box-sizing: border-box; margin: 0; padding: 0; }
  html, body { width: 1200px; height: 972px; overflow: hidden; }
  body { background: var(--canvas); font-family: "Roboto", sans-serif; position: relative; }

  .spread { position: absolute; left: 153px; top: 167px; width: 895px; height: 638px; display: flex; }
  .page { position: relative; width: 50%; height: 100%; overflow: hidden; }

  /* Left page */
  .page--services { background: linear-gradient(180deg, var(--slate) 0%, var(--slate-light) 55%, #3e4457 100%); }
  .hero-left { position: absolute; inset: 0 0 auto 0; height: 245px;
    background: linear-gradient(120deg, #1e2230 0%, #2c3142 50%, #3a4152 100%);
    clip-path: polygon(0 0, 100% 0, 100% 100%, 0 76%); }
  .crowd-photo { position: absolute; left: 0; right: 0; bottom: 0; height: 130px;
    background: linear-gradient(180deg, rgba(62,68,87,0) 0%, #394056 40%, #2c3244 100%); }
  .services-label { position: absolute; left: 32px; top: 221px; color: var(--white); font-size: 11px; }
  .services-label b { font-style: italic; font-weight: 700; }
  .services-label i { font-weight: 400; }

  .service { position: absolute; top: 246px; width: 129px; }
  .service--strategy { left: 24px; }
  .service--operational { left: 160px; }
  .service--tender { left: 296px; }
  .service-icon { display: block; width: 52px; height: 52px; margin: 0 auto; }
  .service-title { margin-top: 13px; text-align: center; color: var(--white); font-size: 10px; font-weight: 700; letter-spacing: 0.2px; }
  .service-card { margin-top: 6px; padding: 5px 6px; border: 1px solid var(--card-line); border-radius: 7px;
    background: var(--card); color: var(--white); font-size: 7.2px; font-style: italic; line-height: 1.27; text-align: justify; }
  .service-card + .service-card { margin-top: 6px; }

  /* Right page */
  .page--roadmap { background: var(--white); }
  .hero-right { position: absolute; inset: 0 0 auto 0; height: 285px;
    background: linear-gradient(135deg, #3a3f4c 0%, #6b6f78 45%, #8c8a86 70%, #4b4f5a 100%);
    clip-path: polygon(0 0, 100% 0, 100% 80%, 0 88%); }
  .hero-rule { position: absolute; left: 0; right: 0; top: 255px; height: 48px; background: var(--rule-grey);
    clip-path: polygon(0 8%, 100% 72%, 100% 100%, 0 40%); }
  .title { position: absolute; left: 36px; top: 306px; color: var(--ink); line-height: 1; }
  .title-light { display: block; font-size: 25px; font-weight: 300; letter-spacing: 0.3px; }
  .title-bold { display: block; font-size: 25px; font-weight: 700; margin-top: 3px; letter-spacing: 0.3px; }
  .subtitle { position: absolute; left: 36px; top: 364px; font-size: 12.5px; font-weight: 500; color: var(--ink); }
  .steps { position: absolute; left: 28px; top: 387px; width: 384px; list-style: none; }
  .step { position: relative; padding-left: 16px; margin-bottom: 10.5px; font-size: 8.2px; line-height: 1.3; color: var(--ink-soft); }
  .step b { font-style: italic; font-weight: 700; color: var(--ink); }
  .step svg { position: absolute; left: 0; top: 1px; width: 10px; height: 9px; }
  .url-band { position: absolute; left: 30px; right: 48px; top: 608px; height: 14px;
    background: linear-gradient(90deg, rgba(58,61,70,0) 0%, var(--band) 18%, var(--band) 82%, rgba(58,61,70,0) 100%);
    color: var(--white); font-size: 9px; letter-spacing: 1.6px; text-align: center; line-height: 14px; }
</style>
</head>
<body>
<main class="spread">

  <section class="page page--services">
    <div class="hero-left" role="img" aria-label="Photo of a hand touching glowing digital gears"></div>
    <div class="crowd-photo" role="img" aria-label="Photo of business people in silhouette"></div>

    <p class="services-label"><b>Services for End</b> <i>User Organisations</i></p>

    <article class="service service--strategy">
      <svg class="service-icon" viewBox="0 0 52 52" aria-hidden="true">
        <circle cx="26" cy="26" r="24" fill="var(--icon-blue)" stroke="#fff" stroke-width="2"/>
        <path d="M19 37v-5c-3-2-5-5-5-9 0-6 5-10 11-10s11 4 11 10l3 5h-3v4c0 2-1 3-3 3h-3v2z" fill="#fff"/>
        <circle cx="23" cy="22" r="3.5" fill="none" stroke="var(--icon-blue)" stroke-width="2"/>
        <circle cx="30" cy="27" r="2.5" fill="none" stroke="var(--icon-blue)" stroke-width="1.8"/>
      </svg>
      <h2 class="service-title">STRATEGY DESIGN</h2>
      <p class="service-card">Strategic design and creation for End Users with either existing strategies around Managed Print Services, Document workflow /automation and digital transformation, or those seeking to implement a totally new approach. We provide trusted and experienced guidance and advice on building a strategy in line with your business and avoiding the many pitfalls.</p>
      <p class="service-card">Mid-term strategic development Services designed to assist End Users in re-vamping or improving existing strategies, especially where complications and issue resolution is required.</p>
    </article>

    <article class="service service--operational">
      <svg class="service-icon" viewBox="0 0 52 52" aria-hidden="true">
        <circle cx="26" cy="26" r="24" fill="var(--icon-blue)" stroke="#fff" stroke-width="2"/>
        <rect x="21" y="12" width="10" height="10" rx="1.5" fill="#fff"/>
        <circle cx="26" cy="11" r="2.5" fill="#fff"/>
        <path d="M12 24l4 10 8 5v-7l-6-4-2-5zM40 24l-4 10-8 5v-7l6-4 2-5z" fill="#fff"/>
      </svg>
      <h2 class="service-title">OPERATIONAL DESIGN</h2>
      <p class="service-card">How much needs to be outsourced and how much can be handled in house when looking at document centric hardware or software solutions? What will provide best value for money while providing a positive end user experience?</p>
      <p class="service-card">Ongoing management of Print &amp; Document environments needs to be carefully considered. Security, visibility, accountability and more are important factors - we can help design and advise based on your business needs.</p>
    </article>

    <article class="service service--tender">
      <svg class="service-icon" viewBox="0 0 52 52" aria-hidden="true">
        <circle cx="26" cy="26" r="24" fill="var(--icon-blue)" stroke="#fff" stroke-width="2"/>
        <circle cx="26" cy="17" r="4" fill="#fff"/>
        <circle cx="17" cy="22" r="3" fill="#fff"/>
        <circle cx="35" cy="22" r="3" fill="#fff"/>
        <path d="M20 38v-10c0-3 3-5 6-5s6 2 6 5v10zM12 38v-8c0-2 2-4 5-4l2 1v11zM40 38v-8c0-2-2-4-5-4l-2 1v11z" fill="#fff"/>
      </svg>
      <h2 class="service-title">TENDER CONSULTANCY</h2>
      <p class="service-card">We provide tender writing services for all types of End Users who are either unsure of how to structure a tender based around Print &amp; Document solutions or who simply do not have the resource available to do so. As with all of our work, this does involve a co-operative approach to ensure your business needs are met within any tender documentation.</p>
      <p class="service-card">Content consultancy – providing non-bias, simple and clear consultancy on areas of content within any tender. If you need assistance on areas such as hardware definition/design, software or workflow requirements, service level specifications or more we can help.</p>
      <p class="service-card">Tender Procurement Services are also provided, allowing End User organisations to hire us to assist with the later stages of a tender process, from supplier selection and analysis right through to implementation support services.</p>
    </article>
  </section>

  <section class="page page--roadmap">
    <div class="hero-right" role="img" aria-label="Photo of a team meeting around laptops and charts"></div>
    <div class="hero-rule"></div>

    <h1 class="title"><span class="title-light">STRATEGY DESIGN</span><span class="title-bold">SERVICES</span></h1>
    <p class="subtitle">A roadmap for your future</p>

    <ul class="steps">
      <li class="step"><svg viewBox="0 0 10 9" aria-hidden="true"><path d="M1 5l3 3 5-7" fill="none" stroke="#3d4250" stroke-width="1.8"/></svg><b>Stakeholder Interviews &amp; Feedback -</b> a key element right at the beginning of the process. It is important for us to understand your organisation in detail, its specific areas of business, target markets, competitors and much more.</li>
      <li class="step"><svg viewBox="0 0 10 9" aria-hidden="true"><path d="M1 5l3 3 5-7" fill="none" stroke="#3d4250" stroke-width="1.8"/></svg><b>Objective &amp; Goal Mapping -</b> where does your organisation need to get to with any new strategic design, what are the risk factors, and what are the key priorities.</li>
      <li class="step"><svg viewBox="0 0 10 9" aria-hidden="true"><path d="M1 5l3 3 5-7" fill="none" stroke="#3d4250" stroke-width="1.8"/></svg><b>Departmental/Process Review -</b> what is done where in the current organisation structure, why and how.</li>
      <li class="step"><svg viewBox="0 0 10 9" aria-hidden="true"><path d="M1 5l3 3 5-7" fill="none" stroke="#3d4250" stroke-width="1.8"/></svg><b>Gap Analysis -</b> understanding the gaps and areas to address between the current state and the short/mid-term and long term objectives and goals.</li>
      <li class="step"><svg viewBox="0 0 10 9" aria-hidden="true"><path d="M1 5l3 3 5-7" fill="none" stroke="#3d4250" stroke-width="1.8"/></svg><b>Strategic Design Proposal -</b> based on all findings the new strategic design proposal can be created. This must then be agreed and signed off by all relevant stakeholders</li>
      <li class="step"><svg viewBox="0 0 10 9" aria-hidden="true"><path d="M1 5l3 3 5-7" fill="none" stroke="#3d4250" stroke-width="1.8"/></svg><b>Final Design &amp; Project Plan -</b> the final critical element is understanding how and more importantly when all elements of the new strategy can be implemented</li>
    </ul>

    <p class="url-band">www.brantwellconsultancy.co.uk</p>
  </section>

</main>
</body>
</html>
```